New Zealand Luggage Importer Needs Business Cards

We need professional, creative and fashionable business cards created.
We are based in New Zealand and import and distribute high-end, quality, fashionable and durable luggage.
We pride ourselves on selling the very best quality luggage, second only to 1 brand (which we won't mention here)...we use the same manufacturer. However, our prices are much more reasonable.
Industry/Entity Type
Business
Contact Information for Business Card
Mark Dunsley
027 512 4068
3/17 Harlow Street, Pinecrest Flats, Auckland, 0614
PO Box 204377, Fernside, Auckland 0731
09-528-3916
sales@brivancases.co.nz / www.brivancases.co.nz

```html
<!DOCTYPE html>
<html lang="en">
<head>
<meta charset="utf-8">
<title>Brivan Cases – Business Card</title>
<link rel="stylesheet" href="https://fonts.googleapis.com/css2?family=Open+Sans:wght@400;600&family=Roboto:wght@400&family=Roboto+Condensed:wght@700&display=swap">
<style>
  :root {
    --page-bg: #e3e3e3;
    --card-dark: #3a3a3a;
    --card-light: #f4f4f4;
    --tone-soft: #fafafa;
    --tone-mid: #e4e4e5;
    --tone-deep: #d4d5d7;
    --text-main: #3c3c3c;
    --text-name: #111111;
    --brand-light: #ffffff;
    --icon: #444444;
  }
  * { margin: 0; padding: 0; box-sizing: border-box; }
  html, body {
    width: 1200px; height: 1000px; overflow: hidden;
    background: var(--page-bg);
  }
  .canvas { position: relative; width: 1200px; height: 1000px; }
  .card {
    position: absolute; overflow: hidden;
    background: var(--card-light);
  }
  .card--logo {
    left: 456px; top: 76px; width: 633px; height: 381px;
    background: var(--card-dark);
  }
  .card--contact { left: 137px; top: 507px; width: 639px; height: 383px; }

  .front-art {
    position: absolute; left: 0; right: 0; bottom: 0; height: 92px;
    background: linear-gradient(90deg, var(--tone-mid) 0%, var(--tone-soft) 55%, var(--tone-deep) 100%);
  }
  .back-art {
    position: absolute; inset: 0;
    background: linear-gradient(120deg, var(--tone-soft) 0%, var(--tone-mid) 40%, var(--tone-deep) 70%, var(--tone-soft) 100%);
  }

  .brand-name {
    position: absolute; left: 0; right: 0; top: 163px;
    text-align: center;
    font-family: "Open Sans", sans-serif; font-weight: 600;
    font-size: 40px; letter-spacing: 3px; color: var(--brand-light);
  }

  .holder-name {
    position: absolute; left: 53px; top: 175px;
    font-size: 24px; color: var(--text-name);
    font-family: "Roboto", sans-serif;
  }
  .holder-name .surname { font-family: "Roboto Condensed", sans-serif; font-weight: 700; }

  .contact-list {
    position: absolute; left: 208px; top: 111px; list-style: none;
    font-family: "Open Sans", sans-serif; font-size: 16px; line-height: 18px;
    color: var(--text-main);
  }
  .contact-list li { position: relative; padding-left: 34px; margin-bottom: 18px; }
  .contact-list .icon { position: absolute; left: 2px; top: 1px; width: 16px; height: 16px; }
</style>
</head>
<body>
<main class="canvas">

  <section class="card card--logo" aria-label="Business card front">
    <div class="front-art" role="img" aria-label="Light grey decorative band along the lower edge"></div>
    <div class="brand-name">BRIVAN CASES</div>
  </section>

  <section class="card card--contact" aria-label="Business card back">
    <div class="back-art" role="img" aria-label="Soft grey decorative background"></div>

    <p class="holder-name">Mark <span class="surname">Dunsley</span></p>

    <ul class="contact-list">
      <li>
        <svg class="icon" viewBox="0 0 16 16" aria-hidden="true"><circle cx="8" cy="8" r="7" fill="none" stroke="var(--icon)" stroke-width="1.3"/><path d="M5.5 4.5l1.4 1.6-.7 1a5 5 0 0 0 2.7 2.7l1-.7 1.6 1.4-.9 1.1C8 11.4 4.6 8 4.4 5.4z" fill="var(--icon)"/></svg>
        027 512 4068
      </li>
      <li>
        <svg class="icon" viewBox="0 0 16 16" aria-hidden="true"><rect x="1" y="4" width="14" height="9" fill="var(--icon)"/><path d="M1 4l7 5 7-5" fill="none" stroke="#fff" stroke-width="1.2"/></svg>
        sales@brivancases.co.nz
      </li>
      <li>
        <svg class="icon" viewBox="0 0 16 16" aria-hidden="true"><g fill="none" stroke="var(--icon)" stroke-width="1.2"><circle cx="8" cy="8" r="6.5"/><ellipse cx="8" cy="8" rx="3" ry="6.5"/><path d="M1.5 8h13M2.5 5h11M2.5 11h11"/></g></svg>
        www.brivancases.co.nz
      </li>
      <li>
        <svg class="icon" viewBox="0 0 16 16" aria-hidden="true"><path d="M8 1a4.5 4.5 0 0 0-4.5 4.5C3.5 9 8 15 8 15s4.5-6 4.5-9.5A4.5 4.5 0 0 0 8 1z" fill="var(--icon)"/><circle cx="8" cy="5.5" r="1.6" fill="#fff"/></svg>
        3/17 Harlow Street, Pinecrest Flats, Auckland, 0614<br>
        PO Box 204377, Fernside, Auckland 0731<br>
        09-528-3916
      </li>
    </ul>
  </section>

</main>
</body>
</html>
```